Haulage company, lets use ruby red white and some 3rd color for web design. and Alder Croft Transport logo

Target Market(s)

Transport industry

Industry/Entity Type

transport

Number of Pages Required

2 page

Requirements
Must have
• Logo

```html
<!DOCTYPE html>
<html lang="en">
<head>
<meta charset="utf-8">
<title>Alder Croft Transport</title>
<link href="https://fonts.googleapis.com/css2?family=Michroma&family=Roboto:wght@400;500;700&display=swap" rel="stylesheet">
<style>
:root{
  --ruby:#a3111f;
  --ruby-deep:#8c0d19;
  --ink:#1c1c1c;
  --text:#333;
  --muted:#9a9a9a;
  --light:#f2f2f2;
  --white:#fff;
  --footer:#1d1d1d;
  --star:#e07a10;
}
*{margin:0;padding:0;box-sizing:border-box}
html,body{width:1200px;height:4229px;overflow:hidden}
body{font-family:'Roboto',Arial,sans-serif;color:var(--text);background:var(--white);position:relative}
.display{font-family:'Michroma',Arial,sans-serif;font-weight:400;letter-spacing:.18em;text-transform:uppercase;color:var(--ink)}
.accent{color:var(--ruby)}
section,footer{position:absolute;left:0;width:1200px}
.abs{position:absolute}
.eyebrow{font-size:15px;color:var(--muted);text-transform:uppercase;text-align:center;width:100%}
.section-title{font-size:32px;text-align:center;width:100%;line-height:1}
.rule{height:3px;width:44px;background:var(--ruby)}
.btn{display:flex;align-items:center;justify-content:center;font-weight:700;font-size:15px;text-transform:uppercase}
.btn-solid{background:var(--ruby);color:var(--white)}
.btn-line{border:2px solid var(--ruby);color:var(--ink);background:var(--white)}
.photo{display:block}
.social{display:flex;gap:8px}
.social span{width:31px;height:31px;display:block}
.social .fill{background:var(--ruby)}
.social .frame{border:2px solid var(--ruby);background:var(--white)}

/* hero */
.hero{top:0;height:750px;overflow:hidden}
.hero-photo{position:absolute;inset:0;background:linear-gradient(180deg,#e8edf2 0%,#d4dde6 28%,#8ea4b8 40%,#5d7a94 52%,#9aa0a4 62%,#6f6f72 78%,#3c3c3e 100%)}
.topbar{position:absolute;left:0;top:0;width:1200px;height:53px;border-bottom:1px solid rgba(0,0,0,.1);font-family:'Michroma',sans-serif;font-size:11px;color:var(--ink)}
.topbar-contact{position:absolute;left:112px;top:19px;display:flex;gap:30px;align-items:center;letter-spacing:.04em}
.topbar .social{position:absolute;left:975px;top:11px}
.nav-bar{position:absolute;left:0;top:53px;width:1200px;height:100px}
.logo{font-family:'Michroma',sans-serif;color:var(--ink);letter-spacing:.2em;line-height:1.35;text-transform:uppercase}
.nav-bar .logo{position:absolute;left:112px;top:14px;font-size:24px}
.nav-bar .logo small{display:block;font-size:18px}
.menu{position:absolute;left:523px;top:40px;display:flex;gap:42px;font-size:16px;font-weight:500;color:var(--ink)}
.menu .on{color:var(--ruby)}
.hero-copy{top:212px;text-align:center;width:100%}
.hero-copy h1{font-size:32px;line-height:1.45;letter-spacing:.2em}
.hero-copy p{font-size:21px;color:var(--ink);width:620px;margin:18px auto 0;line-height:1.42}
.hero .btn{left:522px;top:390px;width:156px;height:47px}
.dots{display:flex;gap:16px;align-items:center}
.hero .dots{position:absolute;left:557px;top:708px}
.hero .dots i{width:6px;height:6px;border-radius:50%;background:var(--white);display:block}
.hero .dots i.on{width:16px;height:16px;border:2px solid var(--white);background:none;position:relative}
.hero .dots i.on:after{content:"";position:absolute;left:3px;top:3px;width:6px;height:6px;border-radius:50%;background:var(--white)}

/* about */
.about{top:750px;height:740px}
.about .eyebrow{position:absolute;left:144px;top:150px;text-align:left;width:auto}
.about h2{position:absolute;left:144px;top:180px;font-size:32px}
.about .rule{position:absolute;left:112px;top:221px}
.about-copy{position:absolute;left:144px;top:250px;width:362px;font-size:15px;line-height:26px;text-align:justify;color:var(--ink)}
.about-copy p+p{margin-top:18px}
.about .btn{left:144px;top:555px;width:147px;height:50px}
.about .photo-large{position:absolute;left:625px;top:135px;width:463px;height:428px;background:linear-gradient(160deg,#b9c8d8 0%,#e6e8ea 35%,#c5c3c1 60%,#7a3a3e 80%,#5f5c5a 100%)}
.about .photo-small{position:absolute;left:563px;top:379px;width:279px;height:245px;background:linear-gradient(180deg,#5f86b8 0%,#c9b7a6 45%,#d9d9d9 60%,#8e2630 80%,#3b3b3b 100%)}

/* services */
.services{top:1490px;height:844px;background:var(--light)}
.services .eyebrow{position:absolute;top:90px}
.services h2{position:absolute;top:118px}
.services .rule{position:absolute;left:578px;top:160px}
.services .lead{position:absolute;left:150px;top:176px;width:900px;text-align:center;font-size:14.5px;line-height:26px;color:var(--ink)}
.card{position:absolute;top:280px;width:303px;height:476px;background:var(--white);box-shadow:0 3px 12px rgba(0,0,0,.12);text-align:center}
.card .photo{position:absolute;left:6px;top:8px;width:291px;height:217px}
.card h3{position:absolute;top:250px;width:100%;font-size:17px;font-weight:500;color:var(--ink)}
.card .dot{position:absolute;left:148px;top:275px;width:7px;height:7px;border-radius:50%;background:var(--ruby)}
.card p{position:absolute;left:18px;top:292px;width:267px;font-size:15.5px;line-height:26px;color:var(--ink)}
.card .btn{left:90px;top:400px;width:123px;height:40px;font-size:13px}
.arrow{position:absolute;top:503px;width:34px;height:34px;border-radius:50%;display:flex;align-items:center;justify-content:center}
.arrow.prev{left:34px;background:#e2e2e2}
.arrow.next{left:1131px;background:var(--ruby)}

/* cta */
.cta{top:2334px;height:411px;background:linear-gradient(100deg,var(--ruby-deep) 0%,#a8141f 45%,#b81d28 70%,#9c1320 100%);text-align:center;color:var(--white)}
.cta .eyebrow{position:absolute;top:78px;color:var(--white)}
.cta h2{position:absolute;top:108px;color:var(--white)}
.cta .rule{position:absolute;left:578px;top:150px;background:var(--white);width:38px}
.cta .lead{position:absolute;left:150px;top:174px;width:900px;font-size:14.5px;font-weight:500;line-height:26px}
.cta .btn{left:522px;top:279px;width:156px;height:50px;background:var(--white);color:var(--ink)}

/* testimonials */
.testimonials{top:2745px;height:609px}
.testimonials .eyebrow{position:absolute;top:100px}
.testimonials h2{position:absolute;top:132px}
.testimonials .rule{position:absolute;left:578px;top:171px}
.review{position:absolute;top:206px;width:306px;height:273px;background:var(--white);box-shadow:0 3px 14px rgba(0,0,0,.12)}
.review .stars{position:absolute;left:23px;top:26px;display:flex;gap:3px}
.review p{position:absolute;left:23px;top:56px;width:260px;font-size:13.5px;line-height:23px;text-align:justify;color:#444}
.review hr{position:absolute;left:23px;top:170px;width:260px;border:0;border-top:1px solid #ddd}
.review .avatar{position:absolute;left:23px;top:193px;width:56px;height:56px;border-radius:50%;background:linear-gradient(135deg,#d8d8d8,#9c9c9c)}
.review .who{position:absolute;left:99px;top:206px}
.review .who b{display:block;font-size:14px;font-weight:500;color:var(--ink)}
.review .who span{font-size:12px;color:#777}
.testimonials .dots{position:absolute;left:571px;top:517px;gap:11px}
.testimonials .dots i{width:5px;height:5px;border-radius:50%;background:#ccc;display:block}
.testimonials .dots i.on{background:var(--ruby)}

/* contact form */
.contact-section{top:3354px;height:481px;background:var(--light)}
.contact-section .eyebrow{position:absolute;top:83px}
.contact-section h2{position:absolute;top:115px}
.contact-section .rule{position:absolute;left:578px;top:154px}
.field{position:absolute;background:var(--white);box-shadow:0 2px 8px rgba(0,0,0,.08);font-size:15px;color:#555;padding:16px 17px}
.contact-section .btn{left:519px;top:352px;width:162px;height:50px}

/* footer */
.footer{top:3835px;height:394px;background:var(--footer);color:var(--white)}
.footer .logo{position:absolute;left:112px;top:180px;font-size:23px;color:var(--white)}
.footer h4{position:absolute;top:72px;font-size:17px;font-weight:700;text-transform:uppercase}
.links{position:absolute;top:126px;list-style:none}
.links li{font-size:14px;height:41px;display:flex;align-items:flex-start;gap:16px;text-transform:uppercase}
.links svg{margin-top:2px}
.info{position:absolute;left:857px}
.info .ico{position:absolute;left:0;width:37px;height:37px;background:var(--white);display:flex;align-items:center;justify-content:center}
.info .txt{position:absolute;left:59px;width:200px;font-size:12px;line-height:19px}
.info .txt b{display:block;font-size:14px;font-weight:700}
.footer .divider{position:absolute;left:112px;top:331px;width:976px;border-top:1px solid #3a3a3a}
.footer-copy{position:absolute;top:352px;width:100%;text-align:center;font-size:12.5px}
.footer .social{position:absolute;left:975px;top:345px}
.footer .social .frame{border-color:var(--white);background:var(--white)}
</style>
</head>
<body>

<section class="hero">
  <div class="hero-photo" role="img" aria-label="Two refrigerated lorries driving along a coastal motorway beside the sea"></div>
  <div class="topbar">
    <div class="topbar-contact">
      <span><span style="color:var(--ruby)">&#9990;</span>&nbsp; +1 (555) 014 2290</span>
      <span>|</span>
      <span><span style="color:var(--ruby)">&#9993;</span>&nbsp; info@aldercrofttransport.com</span>
    </div>
    <div class="social" aria-label="Social links"><span class="fill"></span><span class="frame"></span><span class="frame"></span></div>
  </div>
  <div class="nav-bar">
    <div class="logo">Alder Croft<small>Transport</small></div>
    <nav class="menu"><span class="on">HOME</span><span>ABOUT US</span><span>OUR SERVICES</span><span>BLOG</span><span>CONTACT US</span></nav>
  </div>
  <div class="abs hero-copy">
    <h1 class="display">We are a<br>haulage company</h1>
    <p>Lorem ipsum dolor sit amet, consectetur adipiscing elit, sed do eiusmod incididunt ut laborea.</p>
  </div>
  <a class="abs btn btn-solid">Get Started</a>
  <div class="dots"><i></i><i class="on"></i><i></i><i></i></div>
</section>

<section class="about">
  <div class="eyebrow">Who we are</div>
  <h2 class="display">About <span class="accent">us</span></h2>
  <div class="rule"></div>
  <div class="about-copy">
    <p>Lorem ipsum dolor sit amet, consectetur adipiscing elit, sed do eiusmod tempor incididunt ut labore et dolore magna aliqua. Ut enim ad minim veniam, quis nostrud exercitation ullamco laboris nisi ut aliquip ex ea commodo consequat. Duis aute irure dolor in reprehenderit in voluptate velit esse cillum dolore eu fugiat nulla pariatur.</p>
    <p>Lorem ipsum dolor sit amet, consectetur adipiscing elit, sed do eiusmod tempor incididunt ut labore et dolore magna aliquea.</p>
  </div>
  <a class="abs btn btn-solid">Learn More</a>
  <div class="photo-large" role="img" aria-label="White lorry with refrigerated trailer parked in a depot yard"></div>
  <div class="photo-small" role="img" aria-label="Front of a white and red tractor unit at dusk"></div>
</section>

<section class="services">
  <div class="eyebrow">What we do</div>
  <h2 class="display section-title">Our <span class="accent">services</span></h2>
  <div class="rule"></div>
  <p class="lead">Lorem ipsum dolor sit amet, consectetur adipiscing elit, sed do eiusmod tempor incididunt ut labore et dolore magna aliqua. Ut enim ad minim veniam, quis nostrud exercitation ullamco laboris nisi ut aliquip ex ea commodo consequat. Duis aute irure dolor in reprehenderit in voluptate velit esse cillum dolore eu fugiat nulla pariaturea.</p>
  <div class="arrow prev"><svg width="12" height="12" viewBox="0 0 12 12"><path d="M8 2 4 6l4 4" fill="none" stroke="#555" stroke-width="2"/></svg></div>
  <div class="arrow next"><svg width="12" height="12" viewBox="0 0 12 12"><path d="M4 2l4 4-4 4" fill="none" stroke="#fff" stroke-width="2"/></svg></div>

  <article class="card" style="left:112px">
    <div class="photo" role="img" aria-label="Red lorry on a desert highway at sunset" style="background:linear-gradient(180deg,#c8a27a 0%,#e0b07a 40%,#8a5a3a 65%,#3a3230 100%)"></div>
    <h3>LOREM IPSUM DOLOR</h3><span class="dot"></span>
    <p>Lorem ipsum dolor sit amet, consec adipiscing elit, sed do eiusmod tempor incididunt ut laboreet dolor magna aliqua.</p>
    <a class="abs btn btn-line">Learn More</a>
  </article>
  <article class="card" style="left:448px">
    <div class="photo" role="img" aria-label="Two white and red lorries parked side by side" style="background:linear-gradient(180deg,#d6e2ec 0%,#eef1f3 40%,#c9c9c9 60%,#9a2b35 78%,#bdbdbd 100%)"></div>
    <h3>LOREM IPSUM DOLOR</h3><span class="dot"></span>
    <p>Lorem ipsum dolor sit amet, consec adipiscing elit, sed do eiusmod tempor incididunt ut laboreet dolor magna aliqua.</p>
    <a class="abs btn btn-solid">Learn More</a>
  </article>
  <article class="card" style="left:785px">
    <div class="photo" role="img" aria-label="Red lorry parked at golden hour" style="background:linear-gradient(180deg,#a8aeb0 0%,#c9b99a 40%,#8a3a34 65%,#4a4038 100%)"></div>
    <h3>LOREM IPSUM DOLOR</h3><span class="dot"></span>
    <p>Lorem ipsum dolor sit amet, consec adipiscing elit, sed do eiusmod tempor incididunt ut laboreet dolor magna aliqua.</p>
    <a class="abs btn btn-line">Learn More</a>
  </article>
</section>

<section class="cta" role="img" aria-label="Lorry at night with a ruby red overlay">
  <div class="eyebrow">Get started</div>
  <h2 class="display section-title">Get ready to start?</h2>
  <div class="rule"></div>
  <p class="lead">Lorem ipsum dolor sit amet, consectetur adipiscing elit, sed do eiusmod tempor incididunt ut labore et dolore magna aliqua. Ut enim ad minim veniam, quis nostrud exercitation ullamco laboris nisi ut aliquip ex ea commodo consequat. Duis aute irure dolor in reprehenderit in velit esse cillum dolore eu fugiat nulla pariaturea.</p>
  <a class="abs btn">Get Started</a>
</section>

<section class="testimonials">
  <div class="eyebrow">Testimonials</div>
  <h2 class="display section-title">What our <span class="accent">customers say</span></h2>
  <div class="rule"></div>

  <article class="review" style="left:112px">
    <div class="stars"><svg width="78" height="13" viewBox="0 0 78 13" fill="var(--star)"><g id="st"><path d="M6.5 0l1.9 4.2 4.6.4-3.5 3 1.1 4.5-4.1-2.4-4 2.4 1-4.5L0 4.6l4.6-.4z"/></g><use href="#st" x="16"/><use href="#st" x="32"/><use href="#st" x="48"/><use href="#st" x="64"/></svg></div>
    <p>Lorem ipsum dolor sit amet, consectetur adipiscing elit, sed do eiusmod tempor incididunt ut labore et dolore magna aliqua. Ut enim ad minim veniam, quis nostrud exercitationea.</p>
    <hr><div class="avatar" role="img" aria-label="Customer portrait"></div>
    <div class="who"><b>MARTIN HALE</b><span>United States</span></div>
  </article>
  <article class="review" style="left:448px">
    <div class="stars"><svg width="78" height="13" viewBox="0 0 78 13" fill="var(--star)"><use href="#st"/><use href="#st" x="16"/><use href="#st" x="32"/><use href="#st" x="48"/><use href="#st" x="64"/></svg></div>
    <p>Lorem ipsum dolor sit amet, consectetur adipiscing elit, sed do eiusmod tempor incididunt ut labore et dolore magna aliqua. Ut enim ad minim veniam, quis nostrud exercitationea.</p>
    <hr><div class="avatar" role="img" aria-label="Customer portrait"></div>
    <div class="who"><b>OLIVIA GRANT</b><span>United States</span></div>
  </article>
  <article class="review" style="left:783px">
    <div class="stars"><svg width="78" height="13" viewBox="0 0 78 13" fill="var(--star)"><use href="#st"/><use href="#st" x="16"/><use href="#st" x="32"/><use href="#st" x="48"/><use href="#st" x="64"/></svg></div>
    <p>Lorem ipsum dolor sit amet, consectetur adipiscing elit, sed do eiusmod tempor incididunt ut labore et dolore magna aliqua. Ut enim ad minim veniam, quis nostrud exercitationea.</p>
    <hr><div class="avatar" role="img" aria-label="Customer portrait" style="background:linear-gradient(135deg,#e9a06a,#c0602e)"></div>
    <div class="who"><b>DANIEL BROOKS</b><span>United States</span></div>
  </article>
  <div class="dots"><i></i><i class="on"></i><i></i><i></i></div>
</section>

<section class="contact-section">
  <div class="eyebrow">Contact us</div>
  <h2 class="display section-title">Get in <span class="accent">touch</span></h2>
  <div class="rule"></div>
  <div class="field" style="left:166px;top:182px;width:282px;height:49px">Full Name</div>
  <div class="field" style="left:460px;top:182px;width:280px;height:49px">Phone</div>
  <div class="field" style="left:752px;top:182px;width:282px;height:49px">Email Address</div>
  <div class="field" style="left:166px;top:242px;width:868px;height:94px">Message</div>
  <a class="abs btn btn-solid">Send Message</a>
</section>

<footer class="footer">
  <div class="logo">Alder Croft<br>Transport</div>

  <h4 style="left:445px">Navigation</h4>
  <ul class="links" style="left:445px">
    <li><svg width="14" height="12" viewBox="0 0 14 12"><path d="M1 6l4 4 8-9" fill="none" stroke="var(--ruby)" stroke-width="2"/></svg>Home</li>
    <li><svg width="14" height="12" viewBox="0 0 14 12"><path d="M1 6l4 4 8-9" fill="none" stroke="var(--ruby)" stroke-width="2"/></svg>About Us</li>
    <li><svg width="14" height="12" viewBox="0 0 14 12"><path d="M1 6l4 4 8-9" fill="none" stroke="var(--ruby)" stroke-width="2"/></svg>Our Services</li>
    <li><svg width="14" height="12" viewBox="0 0 14 12"><path d="M1 6l4 4 8-9" fill="none" stroke="var(--ruby)" stroke-width="2"/></svg>Blog</li>
    <li><svg width="14" height="12" viewBox="0 0 14 12"><path d="M1 6l4 4 8-9" fill="none" stroke="var(--ruby)" stroke-width="2"/></svg>Contact Us</li>
  </ul>

  <h4 style="left:647px">Quick Links</h4>
  <ul class="links" style="left:647px">
    <li><svg width="14" height="12" viewBox="0 0 14 12"><path d="M1 6l4 4 8-9" fill="none" stroke="var(--ruby)" stroke-width="2"/></svg>Site Map</li>
    <li><svg width="14" height="12" viewBox="0 0 14 12"><path d="M1 6l4 4 8-9" fill="none" stroke="var(--ruby)" stroke-width="2"/></svg>Privacy Policy</li>
    <li><svg width="14" height="12" viewBox="0 0 14 12"><path d="M1 6l4 4 8-9" fill="none" stroke="var(--ruby)" stroke-width="2"/></svg>Terms of Use</li>
    <li><svg width="14" height="12" viewBox="0 0 14 12"><path d="M1 6l4 4 8-9" fill="none" stroke="var(--ruby)" stroke-width="2"/></svg>Disclaimer</li>
  </ul>

  <h4 style="left:857px">Contact Us</h4>
  <div class="info" style="top:146px">
    <span class="ico"><svg width="14" height="18" viewBox="0 0 14 18"><path d="M7 0a7 7 0 0 0-7 7c0 5 7 11 7 11s7-6 7-11a7 7 0 0 0-7-7zm0 10a3 3 0 1 1 0-6 3 3 0 0 1 0 6z" fill="var(--ruby)"/></svg></span>
    <div class="txt" style="top:-2px"><b>LOCATION:</b>465, Alder Croft Transport,<br>United States</div>
  </div>
  <div class="info" style="top:226px">
    <span class="ico"><svg width="16" height="16" viewBox="0 0 16 16"><path d="M3 1l3 3-2 2c1 2 3 4 6 6l2-2 3 3-2 2C7 15 1 9 1 3z" fill="var(--ruby)"/></svg></span>
    <div class="txt" style="top:-4px"><b>PHONE:</b>+1 (555) 014 2290</div>
  </div>
  <div class="info" style="top:282px">
    <span class="ico"><svg width="16" height="12" viewBox="0 0 16 12"><path d="M0 0h16v12H0z" fill="var(--ruby)"/><path d="M0 0l8 6 8-6" fill="none" stroke="#fff" stroke-width="1.5"/></svg></span>
    <div class="txt" style="top:-4px"><b>EMAIL:</b>info@aldercrofttransport.com</div>
  </div>

  <div class="divider"></div>
  <div class="footer-copy">&copy; 2024 <b>ALDER CROFT TRANSPORT</b> &nbsp;|&nbsp; All Rights Reserved</div>
  <div class="social" aria-label="Social links"><span class="fill"></span><span class="frame"></span><span class="frame"></span></div>
</footer>

</body>
</html>
```